Emergency Vehicle Installer and Security Firm Needs a Business Card

Our company "Corvalta" need a business card for our Emergency Vehicle Equipment Installation and Infrastructure Security Business. We are contract designers, manufacturers and installers for Emergency Vehicle Fleets. This includes installation of Emergency Lights, Sirens, Vehicle Graphics and Radio Communications. We also supply this products to an international market. We also do consultant, and installation of high level security access, alarm and surveillance equipment for medium to large size businesses.

The design should represent a level of trust in our professionalism and expertise. It should visually display our ongoing relationship with the emergency services, but not overtake our commitment to high level security options.

Target Market(s)

Emergency Services and Businesses requiring high level security

Industry/Entity Type

Business

Contact Information for Business Card

*note complete details will be given to the winning designer for revising. The name "Mark Pelling will be used to fill in name".

Mark Pelling
Managing Director
Corvalta NZ Limited
Phone: +64 027 846 20193
Email: mark.pelling@corvalta-example.co.nz

Requirements
Must have
• Card must be in black. Using our logo on the top as supplied. Designers should try having the reverse side as a blurred image of police lights (red and blue) with our logo in greyscale in the centre (this is not particularly a requirement, but feel free to play around with this option).
Nice to have
• A card design that looks good when spot UV printed. A clean compact and graphic design. A grey scale feel on the front (excluding logo, but you can play around with that idea). Rounded smooth text.
Should not have
• Will update this section as designs come through - feel free to submit what you feel would look good.

```html
<!DOCTYPE html>
<html lang="en">
<head>
<meta charset="utf-8">
<title>Corvalta Business Card</title>
<link rel="stylesheet" href="https://fonts.googleapis.com/css2?family=Open+Sans:wght@400;600;700&display=swap">
<style>
  :root {
    --page-bg: #3a3a3c;
    --card-black: #1c1c1d;
    --card-black-edge: #2a2a2b;
    --text-white: #f4f4f4;
    --text-grey: #c9c9c9;
    --accent-red: #e3262b;
    --grad-orange: #f7941d;
    --grad-red: #ee4a2c;
    --grad-purple: #8e5bb5;
    --grad-blue: #1f5a9e;
  }
  * { margin: 0; padding: 0; box-sizing: border-box; }
  html, body {
    width: 1200px; height: 885px; overflow: hidden;
    background: var(--page-bg);
    font-family: "Open Sans", Arial, sans-serif;
  }
  .sheet {
    position: relative; width: 1200px; height: 885px;
    display: flex; flex-direction: column; align-items: center;
    justify-content: center; gap: 30px;
  }
  .card {
    position: relative; width: 700px; height: 400px;
    border-radius: 4px; overflow: hidden;
    box-shadow: 0 14px 30px rgba(0,0,0,.45);
  }
  /* reverse side */
  .card-back {
    background: linear-gradient(100deg, var(--grad-orange) 0%, var(--grad-red) 30%, var(--grad-purple) 65%, var(--grad-blue) 100%);
  }
  .card-back .glow {
    position: absolute; inset: 0;
    background: radial-gradient(circle at 25% 60%, rgba(255,220,120,.35), transparent 45%),
                radial-gradient(circle at 70% 25%, rgba(255,255,255,.2), transparent 40%);
  }
  .card-back .wordmark {
    position: absolute; left: 50%; top: 50%;
    transform: translate(-50%, -50%);
    font-size: 68px; font-weight: 700; letter-spacing: 1px;
    color: var(--text-white); text-transform: uppercase;
  }
  /* front side */
  .card-front {
    background: linear-gradient(135deg, var(--card-black-edge) 0%, var(--card-black) 55%, #141415 100%);
  }
  .card-front .wordmark {
    position: absolute; left: 50px; top: 150px;
    font-size: 56px; font-weight: 700; letter-spacing: 1px;
    color: var(--text-white); text-transform: uppercase;
  }
  .person {
    position: absolute; right: 60px; top: 95px; text-align: left;
  }
  .person-name {
    font-size: 22px; font-weight: 700; letter-spacing: 1px;
    color: var(--text-white); text-transform: uppercase;
  }
  .person-name .surname { color: var(--accent-red); }
  .person-title { font-size: 14px; color: var(--text-grey); margin-top: 2px; }
  .contact {
    position: absolute; right: 40px; top: 240px;
    list-style: none; text-align: right;
    font-size: 15px; color: var(--text-grey); line-height: 1.6;
  }
  .contact li { display: flex; justify-content: flex-end; align-items: center; gap: 8px; }
  .contact svg { width: 14px; height: 14px; fill: var(--accent-red); }
</style>
</head>
<body>
<main class="sheet">
  <section class="card card-back" aria-label="Card reverse">
    <div class="glow" role="img" aria-label="Soft blurred light background in orange, purple and blue"></div>
    <div class="wordmark">Corvalta</div>
  </section>

  <section class="card card-front" aria-label="Card front">
    <div class="wordmark">Corvalta</div>
    <div class="person">
      <p class="person-name">Mark <span class="surname">Pelling</span></p>
      <p class="person-title">Managing Director</p>
    </div>
    <ul class="contact">
      <li>+64 027 846 20193
        <svg viewBox="0 0 24 24" aria-hidden="true"><path d="M6.6 10.8a15.1 15.1 0 0 0 6.6 6.6l2.2-2.2c.3-.3.7-.4 1-.2 1.1.4 2.3.6 3.6.6.6 0 1 .4 1 1V20c0 .6-.4 1-1 1A17 17 0 0 1 3 4c0-.6.4-1 1-1h3.5c.6 0 1 .4 1 1 0 1.3.2 2.5.6 3.6.1.3 0 .7-.2 1z"/></svg>
      </li>
      <li>mark.pelling@corvalta-example.co.nz
        <svg viewBox="0 0 24 24" aria-hidden="true"><path d="M2 5h20v14H2z"/></svg>
      </li>
    </ul>
  </section>
</main>
</body>
</html>
```